TVRB web site redesign

Meridale Linkworks Provisioning service (TVRB) is a diverse technology company specialising in design and installation of fibre optics, network convergence and building services, for commercial clients in Australia, we required a new design of our website to attract new clients, generate sales leads, and provide information about our services to the market. The site and should have a new technology look and feel and be designed in word press. our branding colour is blue.

Target Market(s)

New developments, Construction organisations, Commercial end users, IT managers, Consultants.

Industry/Entity Type

It Company

Number of Pages Required

5+ page

Font styles to use
Sans Serif

Colors
0292cd
3176b5

Requirements
Must have
• key pages.
• Home page with some sizzle, automated pictures running through, I like the look of this competitor website http://www.lumacrest.com.au/ good clean menus and easy to navigate.
• Services page our key services are Fibre optics, Security, Building services,Electrical. I would like the same page layout (Design) for all our services, with a find out more link on each page, manly picture driven with text around our key messaging.
• About us page with space for company profile and directors pictures, bio and contact information.
• Certifications / Accreditations page with have over 20 certifications on different products from suppliers, and a number of licences from governing bodies.
• Current and past projects page with case studies and customer outcomes
• Contact us page with options around what services they require more information on, please keep in mind the site is around generating sales Leeds and being seen as an industry expert.
Nice to have
• RSS feeds, Linked in link, to be placed within the design, Consistent TVRB branding,Same colour blue as our logo Document library for education information, white papers, presentations etc,
• a new technology look and feel, mobile friendly.
Should not have
• boring layout, move away from our cuurent website http://www.tvrbgroup.com.au/
• no e eCommerce store required.

```html
<!DOCTYPE html>
<html lang="en">
<head>
<meta charset="utf-8">
<title>TVRB – Meridale Linkworks Provisioning service</title>
<link href="https://fonts.googleapis.com/css2?family=Lato:wght@400;700&display=swap" rel="stylesheet">
<style>
:root{
  --brand:#0292cd;
  --brand-deep:#3176b5;
  --button:#0a83c0;
  --band:#0d5a7b;
  --title-light:#2aa6e0;
  --ink:#3a3a3a;
  --footer:#1d1d1d;
  --footer-text:#d8d8d8;
  --white:#ffffff;
}
*{margin:0;padding:0;box-sizing:border-box}
html,body{width:729px;height:1200px;overflow:hidden;background:var(--white)}
body{font-family:"Lato",Arial,sans-serif;color:var(--ink);position:relative}
.abs{position:absolute}
.btn{position:absolute;background:var(--button);color:var(--white);display:flex;align-items:center;justify-content:center;white-space:nowrap}

/* header */
.logo{left:76px;top:8px;width:110px;height:52px;display:flex;align-items:center;gap:6px}
.logo-mark{width:14px;height:14px;background:var(--brand)}
.logo-name{font-size:30px;font-weight:700;color:var(--brand);letter-spacing:1px}
.top-btn{top:12px;height:15px;font-size:8.5px}
.account{left:418px;width:56px}
.cart{left:484px;width:57px;justify-content:flex-start;padding-left:3px;gap:6px}
.cart-icon{width:10px;height:10px;background:var(--button)}
.phone{left:553px;top:11px;display:flex;align-items:center;gap:5px;color:var(--button);font-size:14.5px}
.nav{left:310px;top:40px;height:18px;display:flex}
.nav a{background:var(--button);color:var(--white);font-size:8.4px;text-decoration:none;display:flex;align-items:center;padding:0 7.2px;border-right:1px solid #5db7e3}
.nav a:last-child{border-right:none}
.header-rule{left:0;top:64px;width:729px;height:2px;background:var(--brand)}

/* hero */
.hero{left:0;top:66px;width:729px;height:340px;background:radial-gradient(ellipse 60% 70% at 25% 30%,#33c7ff 0%,#0e7fb8 35%,#07334d 65%,#010406 85%)}

/* about */
.about-tag{left:320px;top:422px;width:88px;height:27px;background:var(--button);color:var(--white);font-size:16px;display:flex;align-items:center;justify-content:center}
.about-tag::after{content:"";position:absolute;right:-6px;top:8px;border-left:6px solid var(--button);border-top:5.5px solid transparent;border-bottom:5.5px solid transparent}
.about-text{left:74px;top:462px;width:582px;font-size:8.2px;line-height:12.5px;text-align:center}
.about-more{left:338px;top:532px;width:58px;height:20px;font-size:9px}

/* services */
.services{left:0;top:573px;width:729px;height:209px;background:var(--band)}
.service{position:absolute;top:14px;width:133px;color:var(--white);text-align:center}
.service-photo{width:133px;height:91px}
.service h3{font-weight:400;font-size:13.5px;margin-top:8px;height:18px}
.service p{font-size:7.3px;line-height:12.4px;text-align:justify;height:37px;overflow:hidden;margin-top:2px}
.service .btn{position:relative;width:49px;height:17px;font-size:7.5px;margin:10px auto 0}

/* projects */
.tab{top:795px;height:24px;font-size:8.6px;color:var(--white);display:flex;align-items:center;justify-content:center;background:var(--button)}
.tab-recent{left:76px;width:76px;background:var(--band)}
.tab-past{left:153px;width:76px}
.project{left:76px;top:820px;width:577px;height:193px;background:var(--band)}
.project h2{position:absolute;left:10px;top:11px;font-size:16.3px;font-weight:400;color:var(--title-light)}
.project-text{position:absolute;left:11px;top:38px;width:333px;font-size:7.9px;line-height:12.4px;color:var(--white)}
.project-text p{text-align:justify}
.project-photo{position:absolute;left:369px;top:23px;width:193px;height:144px;border:2px solid var(--white);background:linear-gradient(170deg,#6f8fa0 0%,#8aa38a 45%,#5d7a45 100%)}
.view-btn{left:10px;top:160px;width:68px;height:22px;font-size:8.7px}

/* footer */
.footer{left:0;top:1027px;width:729px;height:173px;background:var(--footer);color:var(--footer-text)}
.col{position:absolute;top:20px}
.col h4{font-size:10.5px;font-weight:400;color:var(--white);padding-bottom:3px;border-bottom:1px solid #8a8a8a;width:83px}
.links{list-style:none;margin-top:8px;font-size:7.6px;line-height:12.5px}
.links li::before{content:"» ";}
.blog-item{display:flex;gap:8px;margin-top:8px}
.blog-thumb{width:34px;height:30px;flex:none;background:linear-gradient(135deg,#0b6fa8,#5fd0ff 50%,#063450)}
.blog-item strong{display:block;font-weight:400;font-size:8.4px;color:var(--white)}
.blog-item span{display:block;font-size:6.8px;line-height:9.5px;text-align:justify;width:89px}
.contact{font-size:7.6px;line-height:11px;margin-top:8px}
.contact div{display:flex;gap:6px;margin-bottom:6px}
.contact svg{flex:none;margin-top:2px}
.social{margin-top:9px;font-size:7.6px}
.social div{display:flex;align-items:center;gap:7px;margin-bottom:6px}
.social i{width:13px;height:13px;background:#5a5a5a;display:block}
</style>
</head>
<body>

<header>
  <div class="abs logo"><span class="logo-mark"></span><span class="logo-name">TVRB</span></div>
  <div class="btn top-btn account">My Account</div>
  <div class="btn top-btn cart"><span class="cart-icon" style="background:#0a6fa3"></span>My Cart</div>
  <div class="abs phone">
    <svg width="13" height="13" viewBox="0 0 14 14"><rect width="14" height="14" rx="2" fill="#0a83c0"/><path d="M4 3c.6-.4 1.2 0 1.5.7l.4 1c.2.5 0 .9-.4 1.2.4 1 1.1 1.8 2.1 2.3.3-.4.8-.6 1.2-.4l1 .4c.7.3 1 .9.7 1.5-.5 1-1.6 1.2-2.7.7C5.6 9.4 4.3 8 3.5 6 3 4.8 3.1 3.6 4 3z" fill="#fff"/></svg>
    1300 482 916
  </div>
  <nav class="abs nav">
    <a>Home</a><a>Services</a><a>About Us</a><a>Certifications</a><a>Current &amp; Past Projects</a><a>Contacts</a>
  </nav>
  <div class="abs header-rule"></div>
</header>

<div class="abs hero" role="img" aria-label="Close-up of glowing blue fibre optic strands on black"></div>

<section>
  <div class="abs about-tag">About Us</div>
  <p class="abs about-text">TVRB is a Communications Integration Company incorporating the expertise of Data and Fibre Optic Communications, ICT and low voltage systems, Security and Application Services. with over five decades of experience and successes in their respected field of expertise. The quality and proven ability of our management and tradespeople, in conjunction with our extensive network of resources, ensures a successful outcome for our clients. At TVRB our mission is to maximise the value of the service offered to our clients and perform these services through a well-managed process, focusing on quality, technical reliability and cost effectiveness.It is our commitment to provide service with the highest professional standard of excellence, integrity and efficiency.</p>
  <div class="btn about-more">Read More</div>
</section>

<section class="abs services">
  <div class="service" style="left:76px">
    <div class="service-photo" role="img" aria-label="Fibre optic cable with coloured strands" style="background:radial-gradient(circle at 60% 50%,#3aa7e6,#0a2a4d 60%,#020814)"></div>
    <h3>Fibre optics</h3>
    <p>It is a long established fact that a reader will be distracted by the readable content of a page when looking at its layout.</p>
    <div class="btn">Read More</div>
  </div>
  <div class="service" style="left:224px">
    <div class="service-photo" role="img" aria-label="Office towers with a security camera and door keypad" style="background:linear-gradient(160deg,#dfe9f2,#7f9cb8 55%,#4a6070)"></div>
    <h3>Security</h3>
    <p>It is a long established fact that a reader will be distracted by the readable content of a page when looking at its layout.</p>
    <div class="btn">Read More</div>
  </div>
  <div class="service" style="left:372px">
    <div class="service-photo" role="img" aria-label="Worker on a lift platform beside a glass facade" style="background:linear-gradient(160deg,#8fb5da,#3b73ad 55%,#24507e)"></div>
    <h3>Building services</h3>
    <p>It is a long established fact that a reader will be distracted by the readable content of a page when looking at its layout.</p>
    <div class="btn">Read More</div>
  </div>
  <div class="service" style="left:520px">
    <div class="service-photo" role="img" aria-label="Row of orange electrical switchboards" style="background:linear-gradient(180deg,#b88a5a,#e2732a 40%,#a8581f)"></div>
    <h3>Electrical</h3>
    <p>It is a long established fact that a reader will be distracted by the readable content of a page when looking at its layout.</p>
    <div class="btn">Read More</div>
  </div>
</section>

<section>
  <div class="abs tab tab-recent">Recent Projects</div>
  <div class="abs tab tab-past">Past projects</div>
  <div class="abs project">
    <h2>Kestrel Valley Telecommunications Backhaul</h2>
    <div class="project-text">
      <p>The installation of Fibre optic back haul for Kestrel Valley New development ‘Verra’ http://www.verrakestrel.com.au/masterplan</p>
      <p>The installation of 4.0 kilometres of telecommunications pit and pipe infrastructure from Harlow Road through to Kestrel Road; by means of open trench and directions drilling. Back Haul Summary. Time and effort was spend liaising with local environmental and council representatives to ensure installation and restoration was carried out to minimise disruption to local residents.</p>
      <p>Once pit and pipe installations were complete; 4.3 kilometres of fibre cabling was installed along the route, which will be connected when the development is ready.</p>
    </div>
    <div class="project-photo" role="img" aria-label="Aerial view of a new residential development"></div>
    <div class="btn view-btn">View Projects</div>
  </div>
</section>

<footer class="abs footer">
  <div class="col" style="left:76px">
    <h4>Quick links</h4>
    <ul class="links">
      <li>Home</li><li>About Us</li><li>IPS</li><li>Recent Projects</li><li>Contact Us</li><li>Blog</li>
    </ul>
  </div>
  <div class="col" style="left:224px">
    <h4>Blog</h4>
    <div class="blog-item">
      <div class="blog-thumb" role="img" aria-label="Blue fibre strands thumbnail"></div>
      <div><strong>Lorem Ipsum is simply</strong><span>Lorem Ipsum is simply dummy text of the printing</span></div>
    </div>
    <div class="blog-item">
      <div class="blog-thumb" role="img" aria-label="Blue cable strands thumbnail"></div>
      <div><strong>Lorem Ipsum is simply</strong><span>Lorem Ipsum is simply dummy text of the printing</span></div>
    </div>
  </div>
  <div class="col" style="left:372px">
    <h4>Contact Us</h4>
    <div class="contact">
      <div><svg width="6" height="8" viewBox="0 0 6 8"><path d="M3 0a3 3 0 0 1 3 3c0 2-3 5-3 5S0 5 0 3a3 3 0 0 1 3-3z" fill="#ddd"/><circle cx="3" cy="3" r="1" fill="#1d1d1d"/></svg><span>Suite 4B, 12-14 Corvel Avenue<br>Norbrook NSW 2168<br>&nbsp;PO Box 2283 NSW 1749</span></div>
      <div><svg width="7" height="7" viewBox="0 0 14 14"><path d="M3 1c1-.6 2 0 2.5 1l.6 1.6c.3.8 0 1.4-.6 1.9.7 1.6 1.8 2.8 3.4 3.6.5-.6 1.2-.9 1.9-.6l1.6.6c1.1.5 1.6 1.5 1 2.5-.8 1.6-2.6 1.9-4.3 1.1C5.8 11.4 3.6 9.2 2.3 6 1.5 4.1 1.6 2.2 3 1z" fill="#ddd"/></svg><span>1300 482 916</span></div>
      <div><svg width="8" height="7" viewBox="0 0 8 6"><rect width="8" height="6" fill="#ddd"/><path d="M0 0l4 3.2L8 0" stroke="#1d1d1d" stroke-width=".8" fill="none"/></svg><span>hello@tvrbmail.com</span></div>
    </div>
  </div>
  <div class="col" style="left:520px">
    <h4>Follows Us</h4>
    <div class="social">
      <div><i></i>Friendsy</div>
      <div><i></i>Chirper</div>
      <div><i></i>RSS</div>
      <div><i></i>Workline</div>
    </div>
  </div>
</footer>

</body>
</html>
```